DRUM requires an exciting new business card

New business card required for DRUM. We are a new market research consultancy and want our brand to be approachable and be contemporary/modern, bold, uncomplicated/simple, and use friendly and easy to read fonts.

A draft website front page is attached to give you a feel (the pictures will be improved over the coming days).

The business card will be printed on 600gsm card, full colour both sides. The card is unique in that it allows one of four colours to be placed within the seam of the card (see http://uk.carddeck-example.com/products/deluxe/business-cards.html)

The logo has been designed in yellow on white, white on yellow, yellow on black and black on yellow - please select whichever you feel most appropriate from the attached document (please use the versions with the tagline). I think my preference is yellow on white for the front, and then yellow or black as the dominant colour on the back.

Telephone numbers will be given next week as they are now being finalised.

Thanks

Target Market(s)

Professionals in large corporates, such as Marketing Managers at Orvana, Fizzwell Soda, Hallbrook etc.

Industry/Entity Type

Market Research

Requirements
Must have
• Daniel Wexford AMRS
drum
Level 4, 27 Larkspur St
Brenton Vale
NSW 2417
Tel: 02 XXXX XXXX
Mob: XXXX XXXXXX
Email: daniel@drumresearch-example.com.au
Web: www.drumresearch-example.com.au

```html
<!DOCTYPE html>
<html lang="en">
<head>
<meta charset="utf-8">
<title>DRUM business card</title>
<link rel="stylesheet" href="https://fonts.googleapis.com/css2?family=Arimo:wght@700&family=Varela+Round&family=Nunito:wght@800&display=swap">
<style>
  :root {
    --brand-yellow: #ffcc00;
    --charcoal: #404040;
    --tagline-grey: #555555;
    --paper: #ffffff;
    --backdrop: #ffffff;
  }
  html, body {
    margin: 0;
    padding: 0;
    width: 1200px;
    height: 900px;
    overflow: hidden;
    background: var(--backdrop);
  }
  .canvas {
    position: relative;
    width: 1200px;
    height: 900px;
  }
  .card {
    position: absolute;
    box-shadow: 0 4px 14px rgba(0,0,0,0.35);
  }

  /* Front */
  .card-front {
    left: 82px; top: 60px;
    width: 566px; height: 380px;
    background: var(--paper);
    overflow: hidden;
  }
  .wordmark {
    position: absolute;
    left: 72px; top: 74px;
    margin: 0;
    font-family: "Nunito", sans-serif;
    font-weight: 800;
    font-size: 172px;
    line-height: 1;
    letter-spacing: -3px;
    color: var(--brand-yellow);
  }
  .tagline {
    position: absolute;
    left: 106px; top: 240px;
    margin: 0;
    font-family: "Varela Round", sans-serif;
    font-size: 24px;
    color: var(--tagline-grey);
  }
  .corner-fold {
    position: absolute;
    right: 0; bottom: 0;
  }

  /* Back */
  .card-back {
    left: 549px; top: 459px;
    width: 572px; height: 384px;
    background: var(--brand-yellow);
    font-family: "Arimo", sans-serif;
    font-weight: 700;
  }
  .name-bar {
    position: absolute;
    left: 56px; top: 60px;
    width: 465px; height: 51px;
    background: var(--charcoal);
  }
  .name-bar svg {
    position: absolute; left: 0; top: 0;
  }
  .name {
    position: absolute;
    left: 27px; top: 10px;
    margin: 0;
    font-size: 29px;
    color: var(--paper);
    letter-spacing: -0.3px;
  }
  .address-panel {
    position: absolute;
    left: 55px; top: 121px;
    width: 193px; height: 193px;
    background: var(--paper);
  }
  .firm-label {
    position: absolute;
    left: 13px; top: 13px;
    width: 126px; height: 26px;
    background: var(--charcoal);
    color: var(--paper);
    font-size: 14px;
    line-height: 26px;
    text-indent: 8px;
  }
  .address {
    position: absolute;
    left: 15px; top: 46px;
    margin: 0;
    font-style: normal;
    font-size: 20px;
    line-height: 25px;
    color: var(--charcoal);
    letter-spacing: -0.3px;
  }
  .phone-panel, .web-panel {
    position: absolute;
    left: 261px;
    width: 259px;
    background: var(--charcoal);
    color: var(--paper);
  }
  .phone-panel { top: 121px; height: 117px; }
  .web-panel { top: 249px; height: 65px; }
  .phone-list {
    margin: 0; padding: 10px 0 0 11px;
    list-style: none;
    font-size: 19px;
    line-height: 23px;
    letter-spacing: -0.2px;
  }
  .web-list {
    margin: 0; padding: 11px 0 0 8px;
    list-style: none;
    font-size: 11.5px;
    line-height: 19px;
    letter-spacing: -0.3px;
  }
</style>
</head>
<body>
<main class="canvas">

  <section class="card card-front" aria-label="Card front">
    <h1 class="wordmark">drum</h1>
    <p class="tagline">insightful research</p>
    <svg class="corner-fold" width="36" height="36" viewBox="0 0 36 36" aria-hidden="true">
      <polygon points="36,0 36,36 0,36" fill="var(--brand-yellow)"/>
    </svg>
  </section>

  <section class="card card-back" aria-label="Card back">
    <div class="name-bar">
      <svg width="10" height="22" viewBox="0 0 10 22" aria-hidden="true">
        <polygon points="0,0 9,10 0,20" fill="var(--brand-yellow)"/>
      </svg>
      <h2 class="name">DANIEL WEXFORD</h2>
    </div>

    <div class="address-panel">
      <div class="firm-label">AMRS drum</div>
      <address class="address">
        Level 4,<br>
        27 Larkspur St<br>
        Brenton Vale<br>
        NSW 2417
      </address>
    </div>

    <div class="phone-panel">
      <ul class="phone-list">
        <li>Tel : 02 XXXX XXXX</li>
        <li>Mob : 02 XXXX XXXX</li>
      </ul>
    </div>

    <div class="web-panel">
      <ul class="web-list">
        <li>Email : daniel@drumresearch-example.com.au</li>
        <li>Web : www.drumresearch-example.com.au</li>
      </ul>
    </div>
  </section>

</main>
</body>
</html>
```